依頼詳細
コラーゲンの錠剤を入れるボトルに貼るシュリンクフィルムのデザインをお願いいたします。
色は白地・薄墨桜色・黒・白・桃色、桜葉色などです。
記載項目
シュリンクフィルムになります。
希望イメージ
シンプル 複雑
単色 カラフル
暗い 明るい
日常 高級
遊び心 厳粛
未来的 伝統的
女性的 男性的
希望する色
薄墨桜葉
納品ファイル
• イラストレーター形式 (.ai)
補足説明
商品コンセプト:
中高年女性の美容と健康のために必要な栄養素のコラーゲンをはじめとする20種類をふんだんに配合したサプリメント。

ブランドイメージ:
創業明治8年の老舗製薬会社である当社は吉野と飛鳥に位置し、信頼・安心・安全なお薬を地域の皆様にご提供してきた。
流行に踊らされない一本筋の通った吉野・飛鳥の厳かで気品に満ちた雰囲気を伝えたい。

イメージカラー:色は白地・薄墨桜色・黒・白・桃色、桜葉色
名    称   :そよぎの雫 コラーゲン
キャッチコピー  : 美しく元気に
カテゴリー名称 : 20種類を凝縮
その他の特徴   :食べやすい(or 安心素材使用)
締切伸ばしました。
■ 選んだ理由

パッケージの名前に力があるのを選ばせて頂きました!

■ 提案者全員のお礼・コメント

本当にたくさんありがとうございました!
コンセプトと世界観をこちらからももっと伝えなければと
反省です。これからもよろしくお願いいたします。

```html
<!DOCTYPE html>
<html lang="ja">
<head>
<meta charset="UTF-8">
<title>そよぎの雫 コラーゲン</title>
<link href="https://fonts.googleapis.com/css2?family=Shippori+Mincho:wght@500;600&display=swap" rel="stylesheet">
<style>
  :root {
    --paper: #ffffff;
    --band: #7a2118;
    --ink: #5b2b1c;
    --sakura-deep: #e8a0aa;
    --sakura-mid: #f3c6cd;
    --sakura-pale: #fcecef;
  }
  html, body {
    margin: 0;
    padding: 0;
    width: 854px;
    height: 1200px;
    overflow: hidden;
    background: var(--paper);
  }
  .label {
    position: relative;
    width: 854px;
    height: 1200px;
    background: var(--paper);
  }
  .top-band {
    position: absolute;
    left: 62px;
    right: 62px;
    top: 108px;
    height: 26px;
    background: var(--band);
  }
  .emblem-circle {
    position: absolute;
    left: 177px;
    top: 268px;
    width: 500px;
    height: 500px;
  }
  .product-name {
    position: absolute;
    left: 50%;
    top: 248px;
    transform: translateX(-50%);
    writing-mode: vertical-rl;
    font-family: "Shippori Mincho", serif;
    font-weight: 500;
    font-size: 66px;
    letter-spacing: 0.14em;
    color: var(--ink);
    margin: 0;
    line-height: 1;
  }
  .category {
    position: absolute;
    left: 0;
    right: 0;
    top: 790px;
    text-align: center;
    font-family: "Shippori Mincho", serif;
    font-weight: 600;
    font-size: 28px;
    letter-spacing: 0.1em;
    color: var(--ink);
    margin: 0;
    line-height: 1;
  }
</style>
</head>
<body>
  <main class="label">
    <div class="top-band"></div>

    <svg class="emblem-circle" viewBox="0 0 500 500" role="img" aria-label="桜色と白の市松模様をあしらった円形の背景">
      <defs>
        <linearGradient id="sakuraFill" x1="0" y1="0" x2="1" y2="1">
          <stop offset="0" stop-color="var(--sakura-mid)"/>
          <stop offset="0.45" stop-color="var(--sakura-pale)"/>
          <stop offset="1" stop-color="var(--sakura-deep)"/>
        </linearGradient>
      </defs>
      <circle cx="250" cy="250" r="250" fill="url(#sakuraFill)"/>
    </svg>

    <h1 class="product-name">そよぎの雫</h1>
    <p class="category">コラーゲン</p>
  </main>
</body>
</html>
```